Life Coaching Business Needs A Business card Design

Earthy, quirky, colourful business card needed for a Life Coaching company supporting same sex attracted young men. My coaching supports these same sex attracted guys to find their own inner happiness and passion and purpose and not feel they need to live a 'label' or follow the crowd. It its about personal passion and happiness.
IT IS ABOUT THEIR INNER RAINBOW.
Some aspects of rainbow would be important to the design.

I have uploaded a recently designed POSTCARD and the business card will be a smaller version with much less information. The Business Card will take the very important parts of the POSTCARD

Front of Card.......
I'm thinking the front of the card would need to be the large LOGO with a rainbow emerging from the inside...from the heart...the core. This will almost FILL the front of the card. This has been uploaded for you. IMMEDIATELY under the LOGO ( to make it a part of the logo) would be the words COACHING * WELLNESS *
The statement HAPPINESS and WHOLENESS for MEN WHO DATE MEN should feature across the front of the BUSINESS CARD as it does across the back of the POSTCARD. It will need some kind of rainbow background to the statement as it does on the POSTCARD. Needs to be a different rainbow pattern. See what you think.

That could be the front. On a black background.
I wonder what you think and what you will do with that.

Back Of Card.

I'm hoping the back of the BUSINESS card could be the PHOTO section from the back of the POSTCARD. The photo and the quote. I will make the quote shorter to fit better on a BUSINESS card. It can be written in a handwriting style to make it look like a personal message from me as it is on the POSTCARD.

All across the top of the back of the card could be the statement
MOTIVATION and INSPIRATION for MEN WHO DATE MEN

Across the card under the statement would be the three contacts
www.velmorquay.com *0437 615 208*tobin@velmorquay.com

It would be great to see if you have a different idea for this arrangement.

At the bottom of the Business card ( as on the photo at on the POSTCARD ) would be my name with a description underneath

Tobin Hadley
Transformational Life Coach * Happiness Guru * Change catalyst

What do you think ? Will all of this work ?
I hope I haven't been too prescriptive. I don't want this to be a boring job for you.

Looking forward to hearing what you think and seeing what you come up with.

Target Market(s)

Same sex attracted males. All ages. Especially those who are struggling or unhappy or depressed. The card must be uplifting and it must SPEAK to these guys. I want ti include a personal 'quote' from me ( in handwriting font as if I wrote to them ) to encourage these guys to get the help they need.

Industry/Entity Type

Business

Contact Information for Business Card

I have been quite prescriptive but am happy to see what the designer might come up with as well. I don't mean to make it boring for the designer. I have included names and contact details in the brief. Please let me know if I need to give you more details.

Requirements
Must have
• LOGO
• A clear statement on the front and back to state clearly who the coaching service is for. I have explained these in the brief.
• Pic of me to fill the back of the card with room to write the details on. I have other pics if needed.
• Needs to be casual and inviting. Almost informal and organic. Quite earthy to balance with the 'lifestyle' these guys can often live.
Nice to have
• Colour and ideas to keep it uncluttered.
Should not have
• Formal design or 'business' like feel.

```html
<!DOCTYPE html>
<html lang="en">
<head>
<meta charset="utf-8">
<title>Tobin Hadley – Coaching Business Card</title>
<link rel="stylesheet" href="https://fonts.googleapis.com/css2?family=Open+Sans:wght@400;700;800&family=Gochi+Hand&display=swap">
<style>
  :root {
    --page-bg: #2b2b2d;
    --card-black: #141516;
    --ink: #1c1c1c;
    --white: #ffffff;
    --sky-top: #f4f8f6;
    --sky-mid: #eef3ea;
    --grass-light: #9dbf5a;
    --grass-dark: #4e7a22;
    --figure-tone: #3a3a36;
    --r-blue: #1f8fd2;
    --r-lilac: #7f81c2;
    --r-slate: #6d7dbb;
    --r-green: #35a84a;
    --r-lime: #98c23b;
    --r-yellow: #f3c300;
    --r-amber: #f4a21c;
    --r-orange: #ee7a22;
    --r-red: #e2382a;
    --r-teal: #1aa0a6;
  }
  html, body {
    margin: 0;
    width: 1200px;
    height: 900px;
    overflow: hidden;
    background: var(--page-bg);
  }
  .business-card {
    position: absolute;
    left: 95px;
    top: 145px;
    width: 1032px;
    height: 600px;
    background: var(--card-black);
    font-family: "Open Sans", Arial, sans-serif;
  }
  .audience-heading {
    position: absolute;
    left: 0;
    right: 0;
    top: 32px;
    margin: 0;
    text-align: center;
    font-size: 27.5px;
    font-weight: 800;
    letter-spacing: 0.2px;
    line-height: 1;
  }
  .photo-panel {
    position: absolute;
    left: 28px;
    top: 75px;
    width: 955px;
    height: 452px;
    overflow: hidden;
    background: linear-gradient(180deg, var(--sky-top) 0%, var(--white) 45%, var(--sky-mid) 78%, var(--grass-light) 81%, var(--grass-dark) 100%);
  }
  .coach-photo-figure {
    position: absolute;
    left: 650px;
    top: 62px;
    width: 180px;
    height: 385px;
    border-radius: 60px 60px 10px 10px;
    background: linear-gradient(180deg, #b89478 0%, var(--figure-tone) 35%, #c9b48c 65%, #b0906f 100%);
    opacity: 0.85;
  }
  .contact-line {
    position: absolute;
    left: 14px;
    top: 6px;
    margin: 0;
    font-size: 26.5px;
    color: var(--ink);
    white-space: nowrap;
    word-spacing: 2px;
  }
  .contact-line span + span { margin-left: 22px; }
  .personal-quote {
    position: absolute;
    left: 88px;
    top: 70px;
    margin: 0;
    font-family: "Gochi Hand", cursive;
    font-size: 41px;
    line-height: 47.5px;
    color: var(--ink);
  }
  .coach-name {
    position: absolute;
    left: 16px;
    top: 393px;
    margin: 0;
    font-size: 37px;
    font-weight: 800;
    color: var(--white);
    letter-spacing: 0.5px;
    text-shadow: -2px -2px 0 #000, 2px -2px 0 #000, -2px 2px 0 #000, 2px 2px 0 #000, 0 3px 0 #000, 3px 0 0 #000, -3px 0 0 #000, 0 -3px 0 #000;
  }
  .services-line {
    position: absolute;
    left: 0;
    right: 0;
    top: 535px;
    margin: 0;
    text-align: center;
    font-size: 23px;
    font-weight: 800;
    white-space: nowrap;
    line-height: 1;
  }
  .c-blue { color: var(--r-blue); }
  .c-lilac { color: var(--r-lilac); }
  .c-slate { color: var(--r-slate); }
  .c-green { color: var(--r-green); }
  .c-lime { color: var(--r-lime); }
  .c-yellow { color: var(--r-yellow); }
  .c-amber { color: var(--r-amber); }
  .c-orange { color: var(--r-orange); }
  .c-red { color: var(--r-red); }
  .c-teal { color: var(--r-teal); }
</style>
</head>
<body>
  <article class="business-card">
    <h1 class="audience-heading">
      <span class="c-blue">COACHING</span>
      <span class="c-lilac">AND</span>
      <span class="c-slate">SUPPORT</span>
      <span class="c-green">FOR</span>
      <span class="c-lime">SAME</span>
      <span class="c-yellow">SEX</span>
      <span class="c-orange">ATTRACTED</span>
      <span class="c-red">GUYS</span>
    </h1>

    <section class="photo-panel">
      <div class="coach-photo-figure" role="img" aria-label="Photo of the coach standing barefoot on a grassy hill in a black singlet and shorts"></div>
      <p class="contact-line">
        <span>www.velmorquay.com</span><span>0437 615 208</span><span>tobin@velmorquay.com</span>
      </p>
      <p class="personal-quote">“My Coaching is about helping to<br>change whatever is making you<br>unhappy or unwell. If you’re not<br>happy, something has to change.<br>If there’s something to change,<br>I can help”</p>
      <h2 class="coach-name">TOBIN HADLEY</h2>
    </section>

    <p class="services-line">
      <span class="c-blue">PERSONAL</span> <span class="c-lilac">CHANGE</span>
      <span class="c-teal">• RELATIONSHIPS</span>
      <span class="c-yellow">• HAPPINESS</span><span class="c-amber">•MINDFULNESS</span>
      <span class="c-red">COACH</span>
    </p>
  </article>
</body>
</html>
```